Short Stage Works Gathering

I need a poster design for our 2012 play festival called 'The Harlow Bay Gathering of Short Stage Works 2012'. We are a community theatre in Port Macquarie, NSW, Australia. A beautiful seaside town with Norfolk Pine Trees and lots of pelicans. Our website is at www.curtaincallstage.org.au for more info. Our logo colours are a vibrant navy blue, red and yellow. The poster would need to depict drama, theatre, our logo, fun, and excitement. The dates are 8 - 10 June 2012. For more information e-mail r.m.dunwell@tidemail.com

Target Market(s)

All age groups and people interested in theatre

Industry/Entity Type

Festival

Requirements
Must have
• Title - Harlow Bay Gathering of Short Stage Works
For more information e-mail r.m.dunwell@tidemail.com
Dates - 8 - 10 June 2012
Curtain Call Stage Logo
Website Address - www.curtaincallstage.org.au
Nice to have
• Background could include a picture of a theatrical stage

```html
<!DOCTYPE html>
<html lang="en">
<head>
<meta charset="utf-8">
<title>Harlow Bay Gathering of Short Stage Works 2012</title>
<link rel="stylesheet" href="https://fonts.googleapis.com/css2?family=Baloo+2:wght@600;700;800&display=swap">
<style>
  :root {
    --stage-black: #120303;
    --curtain-deep: #4a0404;
    --curtain-red: #b3120f;
    --curtain-glow: #e0301a;
    --ember: #b8420e;
    --bronze-light: #e08a3a;
    --bronze: #a34a14;
    --bronze-dark: #4a1606;
    --amber: #f08a1c;
    --gold: #ffd23a;
    --pale-gold: #fff07a;
    --navy: #0d1a4a;
    --night: #050a24;
    --logo-yellow: #ffe23a;
    --logo-navy: #1a2a8c;
  }
  html, body {
    margin: 0;
    padding: 0;
    overflow: hidden;
    background: var(--stage-black);
  }
  .poster {
    position: relative;
    width: 846px;
    height: 1200px;
    overflow: hidden;
    font-family: "Baloo 2", "Trebuchet MS", sans-serif;
    background:
      linear-gradient(to bottom, transparent 80%, var(--navy) 93%, var(--night) 100%),
      radial-gradient(ellipse 70% 45% at 50% 62%, var(--ember) 0%, #6a1a06 55%, var(--stage-black) 100%);
  }
  .stage-curtains {
    position: absolute;
    left: 0;
    top: 0;
    width: 846px;
    height: 620px;
    background:
      radial-gradient(ellipse 40% 50% at 50% 38%, var(--curtain-glow) 0%, var(--curtain-red) 45%, transparent 80%),
      linear-gradient(to right, var(--curtain-deep) 0%, var(--curtain-red) 8%, #7a0a08 18%, transparent 30%, transparent 70%, #7a0a08 82%, var(--curtain-red) 92%, var(--curtain-deep) 100%),
      linear-gradient(to bottom, var(--curtain-red) 0%, var(--curtain-deep) 8%, #8a0c0a 14%, #6a0806 70%, transparent 100%);
  }
  .theatre-masks {
    position: absolute;
    left: 20px;
    top: 590px;
    width: 806px;
    height: 420px;
    border-radius: 40px;
    background:
      radial-gradient(ellipse 28% 42% at 30% 42%, var(--bronze-light) 0%, var(--bronze) 55%, transparent 100%),
      radial-gradient(ellipse 26% 40% at 70% 60%, var(--bronze-light) 0%, var(--bronze) 55%, transparent 100%),
      linear-gradient(to bottom, #8a3a10 0%, var(--bronze-dark) 100%);
  }
  .company-name {
    position: absolute;
    left: 0;
    right: 0;
    top: 70px;
    display: flex;
    flex-direction: column;
    align-items: center;
    gap: 14px;
  }
  .company-name__mark {
    width: 170px;
    height: 170px;
    border-radius: 50%;
    background: var(--logo-navy);
  }
  .company-name__text {
    font-size: 40px;
    font-weight: 700;
    color: var(--logo-yellow);
    line-height: 1;
  }
  .headline {
    position: absolute;
    left: 0;
    right: 0;
    text-align: center;
    margin: 0;
    line-height: 1;
    background: linear-gradient(to bottom, var(--pale-gold) 0%, var(--gold) 35%, var(--amber) 100%);
    -webkit-background-clip: text;
    background-clip: text;
    color: transparent;
    filter: drop-shadow(2px 3px 2px rgba(40, 0, 0, 0.75));
  }
  .headline--place {
    top: 352px;
    font-size: 110px;
    font-weight: 800;
    letter-spacing: 2px;
  }
  .headline--event {
    top: 472px;
    font-size: 50px;
    font-weight: 700;
  }
  .headline--dates {
    top: 530px;
    font-size: 52px;
    font-weight: 700;
  }
  .contact {
    position: absolute;
    left: 0;
    right: 0;
    top: 1020px;
    text-align: center;
  }
  .contact__heading {
    margin: 0 0 10px;
    font-size: 50px;
    font-weight: 700;
    line-height: 1;
    color: var(--amber);
    filter: drop-shadow(2px 2px 1px rgba(0, 0, 0, 0.8));
  }
  .contact__line {
    margin: 0 0 6px;
    font-size: 34px;
    font-weight: 600;
    line-height: 1.25;
    color: var(--gold);
    filter: drop-shadow(1px 2px 1px rgba(0, 0, 0, 0.8));
  }
  .contact__line--web {
    font-size: 36px;
  }
</style>
</head>
<body>
  <main class="poster">
    <div class="stage-curtains" role="img" aria-label="Red velvet stage curtains drawn open around a glowing stage"></div>
    <div class="theatre-masks" role="img" aria-label="Bronze comedy and tragedy theatre masks lit in warm orange light"></div>

    <div class="company-name">
      <span class="company-name__mark"></span>
      <span class="company-name__text">Curtain Call Stage Inc</span>
    </div>

    <h1 class="headline headline--place">Harlow Bay</h1>
    <p class="headline headline--event">Gathering of Short Stage Works</p>
    <p class="headline headline--dates">Dates - 8 - 10 June 2012</p>

    <section class="contact">
      <p class="contact__heading">For More Information</p>
      <p class="contact__line">email r.m.dunwell@tidemail.com</p>
      <p class="contact__line contact__line--web">Visit www.curtaincallstage.org.au</p>
    </section>
  </main>
</body>
</html>
```